Salon and Spa Distributor Business Card

Need a business card. We are are distributor in the salon and spa industry. We identify with natural beauty. Need a card with:
Company Name: Petal Haven"
Title: "President & CEO"
Address
Company Phone number
email
website
Tag Line:" The Professional Salon Source"

Industry/Entity Type

Business

Contact Information for Business Card

Name: Lena Morcott
Title: "President & CEO"
Address: 317 Birchfield Ln, Oakvane, NJ 07481
Company Phone number: 800-463-9152
email: lenamorcott@petalhaven-example.com
website: www.petalhaven-example.com

Requirements
Should not have
• No black backgrounds

```html
<!DOCTYPE html>
<html lang="en">
<head>
<meta charset="utf-8">
<title>Petal Haven – Business Card</title>
<link rel="stylesheet" href="https://fonts.googleapis.com/css2?family=Open+Sans:wght@400;600;700&family=Questrial&display=swap">
<style>
  :root {
    --canvas-bg: #ecebe8;
    --card-white: #ffffff;
    --brand-green: #4a9a3c;
    --brand-green-deep: #0e6e35;
    --brand-green-light: #5cb247;
    --text-grey: #6f6f6f;
    --rule-grey: #d6d6d6;
    --on-green: #ffffff;
  }
  * { box-sizing: border-box; margin: 0; padding: 0; }
  html, body { width: 1200px; height: 1000px; overflow: hidden; }
  body {
    position: relative;
    background: var(--canvas-bg);
    font-family: "Open Sans", Arial, sans-serif;
  }
  .card {
    position: absolute;
    left: 266px;
    width: 666px;
    height: 397px;
    box-shadow: 0 3px 8px rgba(0,0,0,0.18);
    overflow: hidden;
  }
  .card--front { top: 74px; background: var(--card-white); }
  .card--back {
    top: 534px;
    background: radial-gradient(ellipse 520px 420px at 38% 40%, var(--brand-green-light) 0%, #3a9a3e 45%, var(--brand-green-deep) 100%);
  }

  .brand { position: absolute; display: flex; align-items: center; }
  .brand__dot { border-radius: 50%; flex: none; }
  .brand__name { font-family: "Questrial", "Century Gothic", sans-serif; font-weight: 400; white-space: nowrap; }

  .card--front .brand { left: 34px; top: 56px; gap: 18px; }
  .card--front .brand__dot { width: 78px; height: 78px; background: var(--brand-green); }
  .card--front .brand__name { font-size: 38px; color: var(--brand-green); }

  .holder { position: absolute; left: 32px; top: 192px; }
  .holder__name { font-size: 23px; font-weight: 700; color: var(--brand-green); letter-spacing: 0.3px; line-height: 30px; }
  .holder__title { display: flex; align-items: center; gap: 8px; font-size: 15.5px; color: var(--text-grey); line-height: 22px; }
  .holder__rule { width: 190px; height: 2px; background: linear-gradient(90deg, var(--rule-grey), rgba(214,214,214,0)); }

  .contacts { position: absolute; left: 32px; top: 267px; list-style: none; font-size: 16px; color: var(--text-grey); }
  .contacts li { display: flex; align-items: center; gap: 6px; height: 24.5px; }
  .contacts svg { width: 15px; height: 15px; fill: var(--brand-green); flex: none; }
  .contacts .contacts__address { margin-top: 4px; }

  .card--back .brand { left: 117px; top: 150px; gap: 22px; }
  .card--back .brand__dot { width: 110px; height: 110px; background: var(--on-green); }
  .card--back .brand__name { font-size: 44px; color: var(--on-green); }

  .tagline {
    position: absolute; left: 0; right: 0; top: 345px;
    text-align: center; font-size: 18px; color: var(--on-green);
  }
</style>
</head>
<body>

<section class="card card--front" aria-label="Business card front">
  <div class="brand">
    <span class="brand__dot"></span>
    <span class="brand__name">Petal Haven</span>
  </div>

  <div class="holder">
    <p class="holder__name">LENA MORCOTT</p>
    <p class="holder__title">President &amp; CEO <span class="holder__rule"></span></p>
  </div>

  <ul class="contacts">
    <li>
      <svg viewBox="0 0 16 16" aria-hidden="true"><path d="M1 6c0-2 3-3.5 7-3.5S15 4 15 6v1h-3.5V5.5h-7V7H1zM4 8h8l2 5H2z"/></svg>
      800-463-9152
    </li>
    <li>
      <svg viewBox="0 0 16 16" aria-hidden="true"><path d="M1 3h14v1.2L8 8.5 1 4.2zM1 5.8l7 4.3 7-4.3V13H1z"/></svg>
      lenamorcott@petalhaven-example.com
    </li>
    <li>
      <svg viewBox="0 0 16 16" aria-hidden="true"><circle cx="8" cy="8" r="7"/><path d="M1 8h14M8 1c2.5 2 2.5 12 0 14M8 1c-2.5 2-2.5 12 0 14" stroke="#fff" stroke-width="1" fill="none"/></svg>
      www.petalhaven-example.com
    </li>
    <li class="contacts__address">317 Birchfield Ln, Oakvane, NJ 07481</li>
  </ul>
</section>

<section class="card card--back" aria-label="Business card back">
  <div class="brand">
    <span class="brand__dot"></span>
    <span class="brand__name">Petal Haven</span>
  </div>
  <p class="tagline">The Professional Salon Source</p>
</section>

</body>
</html>
```